Modern Can & Tray Design Competition

Please note our brand is now called zé, please do not submit any entries with the wording or logo of "zé kelpwater". Read the full design brief below before making an entry, please.

A competition to design can packaging and outer tray designs for a new exciting brand.

See examples of the design assets I want, below, including both a can and outer tray:

1. https://quillmarketgoods.eu/beverages/energy-drinks/vomba-boost-the-amber-edition-12-x-025-liter-cans-nl/?lang=en

2. https://www.plimvo.com/nl/nl/p/tarvo-fizz-cherry-slim-cans-24-x-330-ml-eu/4812000077312904/

We have 2 flavours in our range, so we need two separate can designs and a separate outer tray design for each flavour.

Our drinks are currently packaged in PET plastic bottles. Our flavours are:
Lemon & Lime - https://zekelpwater.co.uk/products/lemon-and-lime
Strawberry - https://zekelpwater.co.uk/products/strawberry

For this competition, I want can designs for each flavour in 250ml style cans like used by Vomba. And I also want an outer tray for the cans designed for each flavour. Our brand is changing to “zé” so please do not use “kelpwater” on any part of the design. The logo should be “zé” and for each flavour the ze should show the fruit for the flavour embedded inside it. See the files called “ze_fruit_logo_LEMLI (1)” and “ze_fruit_logo_STR (1)” for what I mean. You can use these files for your design.

Under the logo it should state on the can “Prebiotic Fibre Drink”. Similar to how VomBa has “Energy Drink” written under its logo: https://www.drenvilo.com/wp-content/uploads/2009/11/vomba-can-250ml-1.jpg

If you can submit your design ideas for this competition with a picture of the can next to the tray like this for each flavour, that will be best: https://img.keltoshop.com/images/I/57qTzWa2pLx._SL1500_.jpg

So, two design concepts/ideas are needed to enter: One for Lemon & Lime and one for Strawberry.

We want vibrant, eye-catching packaging designs that will catch the consumer's attention.

Right now, we have ze in the centre of our packaging design with fruit embedded in the ze. This must remain a key part of your design as mentioned above. Also, as we will be launching other drinks as a company under different brand names and to unify our different brands we want a splash effect on all the cans which will be replicated across our other brands. So, please have some kind of splash effect on each flavour that can be replicated on the cans of our other brands in future.

Design considerations:

There is also certain information we need on the front/face of the can.

On the very top of the can just below the neck and above the logo we want it to state: “Supports Gut & Overall health*” example: https://pmkgrocerhub.co.uk/wp-content/uploads/2023/10/Brova-Zest-Lemonade.jpg

We also want the number of calories to be stated somewhere on the can in a clever way like in a droplet of the water splash effect. The number of the calories is “17 kcals”.

Under the ze logo as mentioned we want the wording: “Prebiotic Fibre Drink”

Then under Prebiotic Fibre Drink we want the name of the flavour - and then under the flavour we want 3 features stated. Which are:

“20% of daily fibre”
“0g sugar”
“Nothing artificial“

This could be laid out as 3 circles with icons or some other way. The last piece of information under these 3 features is then the size of the can “250 mle”.

In terms of “feel” of the design we want a vibrant colourful feel, and it should show pictures of fruit on it. Here is an example
https://gardenhollowtonics.com/wp-content/uploads/sites/2/2023/03/GHT-US-SodaRange-%E2%80%93-bb-1220x883.png

Any questions let me know. I look forward to seeing your ideas.

To see more about our brand, view our website: www.zekelpwater.co.uk

```html
<!DOCTYPE html>
<html lang="en">
<head>
<meta charset="utf-8">
<title>zé Lemon &amp; Lime can label</title>
<link href="https://fonts.googleapis.com/css2?family=Barlow+Condensed:wght@700&family=Exo+2:ital,wght@0,800;1,300&family=Saira+Condensed:wght@700&family=Lobster&display=swap" rel="stylesheet">
<style>
  :root {
    --backdrop: #dbe65b;
    --band-lime: #d2db2a;
    --band-lime-dark: #aab81a;
    --can-green: #23a640;
    --can-green-dark: #168a33;
    --can-green-light: #3dbb52;
    --navy: #2a2388;
    --navy-dark: #1d1868;
    --zest-yellow: #e0e635;
    --ink: #0d0d0d;
    --soft-white: #e9efe6;
    --splash-lime: #c8e04a;
    --splash-green: #7fbf3a;
  }
  * { margin: 0; padding: 0; box-sizing: border-box; }
  html, body { width: 1200px; height: 1000px; overflow: hidden; }
  body { background: var(--backdrop); position: relative; }

  .can-label {
    position: absolute;
    left: 443px; top: 186px;
    width: 314px; height: 632px;
    border-radius: 10px;
    overflow: hidden;
    background: linear-gradient(90deg, var(--can-green-dark) 0%, var(--can-green-light) 35%, var(--can-green) 65%, var(--can-green-dark) 100%);
    box-shadow: 0 30px 40px -20px rgba(60,70,10,.45);
  }

  .health-band {
    position: absolute; left: 0; top: 0; width: 100%; height: 44px;
    background: linear-gradient(180deg, var(--band-lime) 0%, var(--band-lime-dark) 100%);
    border-bottom: 3px solid #fff;
    display: flex; align-items: center; justify-content: center;
    font-family: "Barlow Condensed", sans-serif; font-weight: 700;
    font-size: 16px; letter-spacing: .3px; color: var(--ink);
    z-index: 3;
  }

  .flavour-name {
    position: absolute; left: 10px; top: 432px;
    width: 348px;
    transform: rotate(-90deg); transform-origin: 0 0;
    font-family: "Lobster", cursive;
    font-size: 50px; line-height: 50px;
    text-align: center;
    color: var(--zest-yellow); white-space: nowrap;
    z-index: 3;
  }

  .brand-name {
    position: absolute; left: 102px; top: 52px;
    font-family: "Exo 2", sans-serif; font-weight: 800;
    font-size: 150px; line-height: 170px;
    color: var(--zest-yellow);
    z-index: 2;
  }

  .product-type {
    position: absolute; left: 108px; top: 272px;
    font-family: "Exo 2", sans-serif; font-style: italic; font-weight: 300;
    font-size: 17px; color: var(--soft-white);
    z-index: 2;
  }

  .feature-list {
    position: absolute; left: 108px; top: 316px;
    list-style: none;
    display: flex; flex-wrap: wrap; column-gap: 12px; row-gap: 9px;
    width: 200px;
    font-family: "Saira Condensed", sans-serif; font-weight: 700;
    font-size: 11px; color: var(--soft-white); letter-spacing: .3px;
    z-index: 2;
  }
  .feature-list li { display: flex; align-items: center; gap: 4px; white-space: nowrap; }
  .feature-icon { width: 13px; height: 13px; }

  .splash-base {
    position: absolute; left: 0; top: 0; width: 100%; height: 100%;
  }

  .calorie-drop {
    position: absolute; left: 250px; top: 372px;
    width: 44px; height: 44px; border-radius: 50%;
    background: var(--navy);
    display: flex; flex-direction: column; align-items: center; justify-content: center;
    font-family: "Saira Condensed", sans-serif; font-weight: 700; color: #fff;
    z-index: 3;
  }
  .calorie-drop .value { font-size: 19px; line-height: 17px; }
  .calorie-drop .unit { font-size: 7px; line-height: 8px; }

  .fruit-splash {
    position: absolute; left: 66px; top: 400px;
    width: 210px; height: 210px; border-radius: 50%;
    background: radial-gradient(circle at 45% 45%, var(--splash-lime) 0%, var(--splash-green) 55%, rgba(200,224,74,.55) 80%, rgba(200,224,74,0) 100%);
    z-index: 1;
  }

  .can-volume {
    position: absolute; left: 8px; top: 566px;
    font-family: "Saira Condensed", sans-serif; font-weight: 700;
    color: #fff; font-size: 24px;
    z-index: 3;
  }
  .can-volume small { font-size: 8px; margin-left: 2px; }
</style>
</head>
<body>
  <main class="can-label">
    <svg class="splash-base" viewBox="0 0 314 632" preserveAspectRatio="none" aria-hidden="true">
      <path d="M0 462 Q30 458 45 460 Q60 444 80 458 L236 454 Q258 462 276 448 Q286 432 292 440 Q296 454 314 454 L314 632 L0 632 Z" fill="var(--navy)"/>
      <path d="M8 462 Q6 432 14 424 Q22 432 18 462 Z" fill="var(--navy-dark)"/>
      <path d="M280 450 Q278 424 288 420 Q296 428 290 454 Z" fill="var(--navy-dark)"/>
    </svg>

    <div class="health-band">SUPPORTS GUT &amp; OVERALL HEALTH</div>

    <div class="flavour-name">Lemon &amp; Lime</div>

    <div class="brand-name">zé</div>

    <p class="product-type">Prebiotic Fibre Drink</p>

    <ul class="feature-list">
      <li>
        <svg class="feature-icon" viewBox="0 0 14 14" aria-hidden="true"><circle cx="7" cy="7" r="7" fill="var(--zest-yellow)"/><path d="M7 3 Q10 7 7 11 Q4 7 7 3Z" fill="var(--can-green-dark)"/></svg>
        20% OF DAILY FIBRE
      </li>
      <li>
        <svg class="feature-icon" viewBox="0 0 14 14" aria-hidden="true"><circle cx="7" cy="7" r="7" fill="var(--zest-yellow)"/><rect x="4.5" y="4.5" width="5" height="5" fill="none" stroke="var(--can-green-dark)" stroke-width="1.2"/><line x1="3" y1="11" x2="11" y2="3" stroke="var(--can-green-dark)" stroke-width="1.2"/></svg>
        0G SUGAR
      </li>
      <li>
        <svg class="feature-icon" viewBox="0 0 14 14" aria-hidden="true"><circle cx="7" cy="7" r="7" fill="var(--zest-yellow)"/><line x1="4" y1="10" x2="10" y2="4" stroke="var(--can-green-dark)" stroke-width="1.6" stroke-linecap="round"/></svg>
        NOTHING ARTIFICIAL
      </li>
    </ul>

    <div class="fruit-splash" role="img" aria-label="Halved lime with mint leaves inside a bright lime-juice splash with flying droplets"></div>

    <div class="calorie-drop"><span class="value">17</span><span class="unit">KCALS</span></div>

    <div class="can-volume">250<small>MLE</small></div>
  </main>
</body>
</html>
```